Family Farm Business Requires Flyer for local CSA retail sales and local advertising

We need a flyer design for our small farm to help promote our CSA business. A CSA is when someone pre-pays for a summer's worth of produce, fruit, and eggs that are raised on our farm. They receive a weekly box of produce and essentially they buy a small share of the summer's bounty. We had a logo designed by someone here on pixel hive so we would like the flyer to include the colors of the logo. The final design should reflect the different options for people the choose and then invite them to sign up to be a CSA Customer.

Target Market(s)

Busy families and moms who are limited in time to buy groceries or healthy food or produce. People who are passionate about local food and local produce.

Industry/Entity Type

Advertising

Font styles to use
Decorative
Script

Requirements
Must have
• Our logo, our farm information (website, social media, location) and contact info as well as the various options to choose from for our CSA farm share. I also included a picture of our business card so it would be good if it matched the colors/style of our card. Also the flyer will be printed on 8.5 x 11 paper and it will be double sided.

```html
<!DOCTYPE html>
<html lang="en">
<head>
<meta charset="utf-8">
<title>Maple Hollow Farm CSA Flyer</title>
<link href="https://fonts.googleapis.com/css2?family=Roboto+Condensed:wght@400;700&family=Roboto:wght@400&display=swap" rel="stylesheet">
<style>
  :root {
    --farm-green: #1f8a45;
    --deep-green: #1d6f3a;
    --leaf-pale: #c9e5c0;
    --tile-pale: #d3e9cb;
    --stem-green: #3fae49;
    --ink: #1c1c1c;
    --glow-yellow: #eef6b8;
    --grass-light: #b7e36a;
    --grass-dark: #5fb52e;
    --gem-green: #8fcb86;
  }
  html, body { margin: 0; padding: 0; overflow: hidden; }
  body { width: 1200px; height: 777px; background: #fff; font-family: "Roboto Condensed", sans-serif; color: var(--ink); }
  p, h1 { margin: 0; }
  .flyer { position: relative; width: 1200px; height: 777px; overflow: hidden; display: flex; }
  .page { position: relative; width: 600px; height: 777px; overflow: hidden; }
  .page-backdrop {
    position: absolute; inset: 0;
    background:
      radial-gradient(ellipse 420px 260px at 50% 0%, var(--glow-yellow), transparent 70%),
      radial-gradient(ellipse 300px 200px at 0% 10%, #e6f3b0, transparent 70%),
      radial-gradient(ellipse 300px 200px at 100% 10%, #e6f3b0, transparent 70%),
      #fbfdf4;
  }
  .grass-band {
    position: absolute; left: 0; right: 0; bottom: 0; height: 120px;
    background: linear-gradient(to bottom, rgba(183,227,106,0) 0%, var(--grass-light) 35%, var(--grass-dark) 100%);
  }
  /* Front page */
  .name-dot { position: absolute; left: 296px; top: 14px; width: 30px; height: 30px; border-radius: 50%; background: var(--farm-green); }
  .farm-name {
    position: absolute; left: 196px; top: 70px; width: 230px;
    text-align: center; font-weight: 700; font-size: 46px; line-height: 1.05;
    color: var(--farm-green); text-transform: uppercase; letter-spacing: 2px;
  }
  .farm-name .town { display: block; font-size: 16px; letter-spacing: 1px; margin-top: 12px; }
  .tagline {
    position: absolute; left: 0; width: 600px; top: 303px; text-align: center;
    font-family: "Roboto", sans-serif; font-size: 29px; line-height: 36px; color: var(--deep-green);
  }
  .tagline .sep { color: var(--stem-green); font-size: 20px; vertical-align: 4px; margin: 0 6px; }
  .share-options-art {
    position: absolute; left: 168px; top: 385px; width: 277px; height: 332px;
    border-radius: 26px;
    background: linear-gradient(to bottom, var(--tile-pale) 0%, #c4e2b4 70%, rgba(196,226,180,0) 100%);
  }
  /* Back page */
  .info-leaf { position: absolute; left: 0; top: 0; }
  .info-text {
    position: absolute; left: 700px; top: 40px; width: 400px;
    text-align: center; font-size: 9.6px; line-height: 11.8px;
  }
  .info-text p { margin: 0 0 6.4px; }
  .info-text .season { color: var(--farm-green); margin: 0 0 3px; }
  .info-text .season-last { margin-bottom: 6.4px; }
  .contact { position: absolute; left: 1006px; top: 568px; font-size: 14px; line-height: 17px; font-style: normal; }
  .contact .phone { font-weight: 700; font-size: 23px; line-height: 28px; color: var(--deep-green); }
  .contact .web { font-weight: 700; color: var(--deep-green); }
</style>
</head>
<body>
<div class="flyer">
  <section class="page page-front">
    <div class="page-backdrop" role="img" aria-label="Soft yellow-green bokeh light background"></div>
    <div class="grass-band" role="img" aria-label="Fresh green grass along the bottom edge"></div>
    <span class="name-dot"></span>
    <h1 class="farm-name">Maple Hollow Farm<span class="town">Brookdale, VA</span></h1>
    <p class="tagline">Fresh<span class="sep">•</span>Local<span class="sep">•</span>Sustainable</p>
    <div class="share-options-art" role="img" aria-label="Illustration of a four-leaf plant whose leaves hold badges for farm fresh, local, home grown vegetables and free range eggs, each above a small pot"></div>
  </section>

  <section class="page page-back">
    <div class="page-backdrop" role="img" aria-label="Soft yellow-green bokeh light background"></div>
    <div class="grass-band" role="img" aria-label="Fresh green grass along the bottom edge"></div>
  </section>

  <svg class="info-leaf" width="1200" height="777" viewBox="0 0 1200 777" aria-hidden="true">
    <path d="M900 0 C960 80 1125 170 1125 283 C1125 370 1000 440 900 560 C800 440 675 370 675 283 C675 170 840 80 900 0 Z" fill="var(--leaf-pale)"/>
    <path d="M912 571 L945 611 L912 651 L879 611 Z" fill="var(--gem-green)"/>
    <path d="M912 660 L929 677 L912 694 L895 677 Z" fill="var(--gem-green)"/>
  </svg>

  <div class="info-text">
    <p>• A small family run<br>produce and orchard farm.</p>
    <p>• We are passionate about local<br>food and serving our community.</p>
    <p>• All Produce &amp; Fruit grown using<br>Organic/Biological best practices, which in turn<br>keeps chemical pesticide and fertilizer use to a minimum.</p>
    <p>• Our goal is a sustainable farm and land that uses crop rotation<br>and cover crops to build and amend the soil and provide<br>the best quality produce and fruit in this area.</p>
    <p>• We also sell free range, pastured eggs. Our “girls” (hens) are truly free range…<br>they roam our 6 acres eating whatever suits their fancy. We also supplement them<br>with non-GMO feed.</p>
    <p>• We are committed to planting non-GMO seed as well as planting many heirloom varieties of seed<br>to keep the past alive and bring back tastes and flavors from the past.</p>
    <p>• We are planning on an 18 week share than begins in June and will run to mid-October. Because<br>of our climate and temps the summer stock will start coming in early to mid July and run through<br>August.</p>
    <p>• Here’s what you could roughly expect for summer:</p>
    <p class="season">June- (Broccoli, Cabbage, Sugar Snap Peas, Various Lettuces, Spinach, Kale, Swiss Chard, Beets)</p>
    <p class="season">July - (Broccoli, Lettuces, Kale, Snow Peas, Summer Squash, Zucchini, Cucumbers, Slicing<br>Tomatoes, Cherry Tomatoes, Green Beans, October Beans, White &amp; Yellow Corn)</p>
    <p class="season season-last">August - (Same as July also - Various Bell Peppers, Sweet Peppers,<br>Hot Peppers, Sweet onions)</p>
    <p>September/Mid-October (much the same as July/August along with<br>several different varieties of potatoes along with a few surprises :)</p>
    <p>• Summer Fruit options: Peaches, Pears, and Blackberries<br>starting in July and would run<br>likely for 3-4 weeks, and then starting in September<br>we will have several different Apple varieties<br>(cooking and eating).</p>
    <p>• The egg share would be a<br>dozen free range, pastured<br>large brown<br>eggs weekly.</p>
  </div>

  <address class="contact">
    Daniel &amp; Mara<br>Whitcombe<br>
    <span class="phone">(555) 013-2847</span><br>
    1180 Orchard Lane<br>
    Brookdale, Virginia 24000<br>
    <span class="web">www.maplehollowfarm.com</span>
  </address>
</div>
</body>
</html>
```